Best website on the WWW

I am looking to create a multi tab wesbite to revamp our outdated website.

Here is an example of a companies website I really like
https://ridgelinehaulers.example/

Target Market(s)

New customers, government agency's

Industry/Entity Type

Auto repair, towing and recovery, hazmat clean up

Coding

Coded - Design and coding required

Number of Pages Required

5+ page

Font styles to use
Sans Serif

Requirements
Nice to have
• I would like to see an interactive website, that includes details and photos from our companies

```html
<!DOCTYPE html>
<html lang="en">
<head>
<meta charset="utf-8">
<title>Harbor Point Repair &amp; Towing</title>
<link rel="stylesheet" href="https://fonts.googleapis.com/css2?family=Poppins:wght@400;500;600&display=swap">
<style>
:root{
  --crimson:#a80d40;
  --crimson-dark:#8e0a35;
  --navy:#0c2350;
  --ink:#111;
  --white:#fff;
  --muted:#666;
}
*{margin:0;padding:0;box-sizing:border-box}
html,body{width:1200px;height:2338px;overflow:hidden}
body{position:relative;font-family:'Poppins',sans-serif;color:var(--ink);background:var(--white)}
.abs{position:absolute}
.topbar{left:0;top:0;width:1200px;height:27px;background:var(--crimson);color:var(--white);font-size:9px;display:flex;align-items:center;padding:0 105px;gap:28px}
.topbar .hours{margin-left:auto}
.topbar span{display:flex;align-items:center;gap:6px;white-space:nowrap}
.topbar .hours b{margin-right:3px}
.header{left:0;top:27px;width:1200px;height:78px}
.brand{left:105px;top:22px;font-size:18px;font-weight:600;color:var(--navy);display:flex;align-items:center;gap:8px}
.brand i{display:block;width:14px;height:14px;background:var(--crimson);border-radius:50%}
.help{left:783px;top:20px;display:flex;align-items:center;gap:10px}
.help .ring{width:30px;height:30px;border:2px solid var(--crimson);border-radius:50%;display:flex;align-items:center;justify-content:center}
.help p{font-size:12px;line-height:15px;font-weight:500}
.help b{color:var(--crimson);font-weight:600}
.social{left:958px;top:22px;display:flex;gap:5px}
.social i{display:block;width:31px;height:31px;border-radius:50%;background:#000}
.nav{left:0;top:105px;width:1200px;height:33px;background:var(--navy);color:var(--white)}
.nav .tag{position:absolute;left:105px;top:10px;font-size:9px}
.nav ul{position:absolute;left:600px;top:0;display:flex;list-style:none;height:33px}
.nav li{font-size:12px;font-weight:500;padding:0 14px;line-height:33px}
.nav li.active{background:var(--crimson)}
.nav .search{position:absolute;left:1081px;top:10px}
.hero{left:0;top:138px;width:1200px;height:536px;background:linear-gradient(90deg,#2c2f35 0%,#555a61 45%,#9a9ea4 75%,#c9ccd0 100%)}
.hero h1{position:absolute;left:105px;top:60px;color:var(--white);font-size:39px;font-weight:600;line-height:50px}
.hero p{position:absolute;left:105px;top:222px;width:370px;color:#eee;font-size:12px;line-height:22.5px}
.btn{display:inline-block;background:var(--crimson);color:var(--white);font-weight:600;font-size:13px;text-align:center}
.hero .btn{position:absolute;left:105px;top:329px;width:214px;height:44px;line-height:44px}
.badges{left:105px;top:594px;width:990px;height:80px;background:var(--white);border-radius:6px 6px 0 0;display:flex;align-items:center;justify-content:space-around;padding:0 40px}
.badges i{display:block;background:#d9d9de}
.welcome{left:105px;top:725px;width:410px}
.welcome h2,.notice h2{font-size:22px;font-weight:600;margin-bottom:6px}
.welcome p,.notice p{font-size:12px;line-height:22.5px}
.welcome .btn{margin-top:33px;width:199px;height:44px;line-height:44px}
.notice{left:105px;top:993px;width:410px}
.notice h3{font-size:15px;font-weight:600;margin-bottom:10px}
.shop-photo{left:629px;top:709px;width:466px;height:465px;background:linear-gradient(160deg,#8a8e93,#3b4a75 40%,#6b6f72 70%,#8d2a2a)}
.band{left:0;top:895px}
.service-title{left:0;top:1325px;width:1200px;text-align:center;color:var(--white);font-size:22px;font-weight:600}
.card{top:1376px;width:321px;height:374px;overflow:hidden}
.card .photo{width:100%}
.card .body{background:var(--crimson);color:var(--white);padding:44px 40px 0 50px}
.card h4{font-size:15px;font-weight:600;text-align:center}
.card .body h4{text-align:left;margin-bottom:26px}
.card .body p{font-size:12px;line-height:22.5px}
.card .bar{height:72px;display:flex;align-items:center;justify-content:center;color:var(--white)}
.newsletter{left:0;top:1814px;width:1200px;height:235px;background:var(--navy);color:var(--white);text-align:center}
.newsletter small{display:block;margin-top:50px;font-size:11px;letter-spacing:4px}
.newsletter h2{font-size:35px;font-weight:400;margin-top:2px}
.newsletter form{position:absolute;left:360px;top:134px;width:481px;height:50px;background:var(--white);border-radius:3px}
.newsletter form span{position:absolute;left:16px;top:17px;color:#777;font-size:11.5px}
.newsletter form b{position:absolute;right:8px;top:7px;width:110px;height:36px;line-height:36px;background:var(--crimson);font-size:12px;font-weight:500;letter-spacing:1.5px}
.footer{left:0;top:2049px;width:1200px;height:289px;background:var(--crimson);color:var(--white)}
.footer .logo-box{position:absolute;left:106px;top:42px;width:124px;height:83px;background:var(--white);color:var(--navy);font-weight:600;font-size:14px;display:flex;align-items:center;justify-content:center;text-align:center;line-height:17px}
.fcol{position:absolute;top:40px}
.fcol h5{font-size:14px;font-weight:400;padding-bottom:6px;border-bottom:1px solid rgba(255,255,255,.25);width:140px;margin-bottom:12px}
.fcol li{list-style:none;font-size:8.5px;line-height:24px}
.fcol.connect h5{width:180px}
.fcol.connect li{display:flex;gap:8px;align-items:flex-start;line-height:18px;margin-bottom:11px}
.fcol.connect li i{flex:none;width:20px;height:20px;border-radius:50%;background:#d6e2ff;margin-top:-2px}
.footer .rule{position:absolute;left:0;top:240px;width:1200px;border-top:1px solid rgba(255,255,255,.2)}
.footer .legal{position:absolute;left:105px;top:259px;width:990px;font-size:9px;display:flex;justify-content:space-between}
</style>
</head>
<body>

<div class="abs topbar">
  <span><svg width="10" height="12" viewBox="0 0 10 12"><path d="M5 0a4 4 0 0 0-4 4c0 3 4 8 4 8s4-5 4-8a4 4 0 0 0-4-4z" fill="#fff"/><circle cx="5" cy="4" r="1.5" fill="#a80d40"/></svg>2280 Lakeview Road, Fairhaven, Ohio 44190, United States</span>
  <span><svg width="13" height="9"><rect width="13" height="9" fill="#fff"/><path d="M0 0l6.5 5L13 0" stroke="#a80d40" fill="none"/></svg>SERVICE@HARBORPOINT.EXAMPLE</span>
  <span class="hours"><svg width="11" height="11"><circle cx="5.5" cy="5.5" r="4.5" stroke="#fff" fill="none"/><path d="M5.5 3v3h2" stroke="#fff" fill="none"/></svg><b>Mechanical Service :</b>Mon to Fri 08:00 am – 05:00 pm, Sat 08:00 am – 01:00 pm, Sun - Closed</span>
</div>

<header class="abs header">
  <div class="abs brand"><i></i>Harbor Point</div>
  <div class="abs help">
    <div class="ring"><svg width="14" height="14" viewBox="0 0 24 24"><path d="M6.6 10.8a15 15 0 0 0 6.6 6.6l2.2-2.2c.3-.3.7-.4 1-.2 1.1.4 2.3.6 3.6.6.6 0 1 .4 1 1V20c0 .6-.4 1-1 1A17 17 0 0 1 3 4c0-.6.4-1 1-1h3.5c.6 0 1 .4 1 1 0 1.3.2 2.5.6 3.6.1.3 0 .7-.2 1z" fill="#a80d40"/></svg></div>
    <p>Need a Help ?<br><b>(555) 014-2290</b></p>
  </div>
  <div class="abs social"><i></i><i></i><i></i><i></i></div>
</header>

<nav class="abs nav">
  <span class="tag">Towing open 24 Hours and 7 days a week</span>
  <ul>
    <li class="active">HOME</li><li>ABOUT US</li><li>MONTHLY COUPONS</li><li>SERVICES</li><li>MORE ⌄</li>
  </ul>
  <svg class="search" width="12" height="12"><circle cx="5" cy="5" r="4" stroke="#fff" stroke-width="1.5" fill="none"/><path d="M8 8l3.5 3.5" stroke="#fff" stroke-width="1.5"/></svg>
</nav>

<section class="abs hero" role="img" aria-label="Heavy wrecker tow truck parked on a snowy roadside">
  <h1>TOWING, AUTO<br>&amp; TRUCK REPAIR.<br>FAMILY OWNED</h1>
  <p>We specialize in Towing, Auto Repair and most Truck Repairs of any size. From driving your daily pickup to your fleet of vehicles auto and truck repair towing service.</p>
  <a class="btn">SHOP VERIFIED REVIEWS</a>
</section>

<div class="abs badges" aria-label="Partner and association badges">
  <i style="width:100px;height:44px;border-radius:4px"></i>
  <i style="width:122px;height:50px;clip-path:polygon(50% 0,100% 50%,50% 100%,0 50%)"></i>
  <i style="width:46px;height:46px;border-radius:50%"></i>
  <i style="width:54px;height:50px;border-radius:4px"></i>
  <i style="width:50px;height:50px;border-radius:50%"></i>
  <i style="width:136px;height:52px;border-radius:26px"></i>
  <i style="width:136px;height:30px;border-radius:4px"></i>
</div>

<section class="abs welcome">
  <h2>WELCOME</h2>
  <p>We now provide our customers with the ability to check their vehicle history on line! We will also send you email reminders when it is time to have your vehicle serviced according to your specific vehicle manufacture. Ask us how to get you registered today!</p>
  <a class="btn">MY VEHICLE HISTORY</a>
</section>

<section class="abs notice">
  <h2>SPECIAL NOTICE</h2>
  <h3>We are open for business!</h3>
  <p>Repair technicians are on the essential list of the Dept of Homeland Security and Harbor Point Repair &amp; Towing is still open during this time.</p>
</section>

<div class="abs band">
  <svg width="1200" height="640" role="img" aria-label="Tow truck hooked to a heavy rig, shown in a diagonal band">
    <defs><linearGradient id="bandTone" x1="0" y1="1" x2="1" y2="0"><stop offset="0" stop-color="#2a2d33"/><stop offset=".6" stop-color="#3f4a55"/><stop offset="1" stop-color="#5c6670"/></linearGradient></defs>
    <polygon points="1200,0 1200,632 0,635 0,575 90,520 300,420" fill="url(#bandTone)"/>
    <polygon points="0,575 110,520 110,635 0,635" fill="#8e1a2c"/>
  </svg>
</div>
<div class="abs shop-photo" role="img" aria-label="White service truck raised on a blue two-post lift inside the repair shop"></div>

<h2 class="abs service-title">FAST AND FRIENDLY CUSTOMER SERVICE</h2>

<article class="abs card" style="left:105px">
  <div class="photo" role="img" aria-label="Close view of an engine during repair" style="height:131px;background:linear-gradient(135deg,#4a4a4a,#9a9a9a 50%,#2c2c2c)"></div>
  <div class="body" style="height:243px">
    <h4>EXPERIENCED TECHNICIANS</h4>
    <p>The mechanics at our shop have over 60 years of experience between them. They are dedicated to providing high-quality repairs to keep you safe and happy.</p>
  </div>
</article>
<article class="abs card" style="left:440px">
  <div class="photo" role="img" aria-label="Technician mounting chrome wheels on a tire machine" style="height:302px;background:linear-gradient(160deg,#6b4a3a,#8a7f78 45%,#3f4658)"></div>
  <div class="bar" style="background:var(--crimson)"><h4>COMPETITIVE PRICING</h4></div>
</article>
<article class="abs card" style="left:775px">
  <div class="photo" role="img" aria-label="Mechanic working at a red tool chest in the shop" style="height:302px;background:linear-gradient(160deg,#4f8a4a,#9a9488 40%,#8e2a2a 75%,#3a3a3a)"></div>
  <div class="bar" style="background:var(--navy)"><h4>OUR QUALITY PROMISE</h4></div>
</article>

<section class="abs newsletter">
  <small>SUBSCRIBE OUR</small>
  <h2>Newsletter</h2>
  <form><span>Enter your email address</span><b>SEND NOW</b></form>
</section>

<footer class="abs footer">
  <div class="logo-box">Harbor Point<br>Repair &amp; Towing</div>
  <div class="fcol" style="left:351px"><h5>MENU</h5><ul><li>ABOUT US</li><li>MONTHLY COUPONS</li><li>SERVICES</li></ul></div>
  <div class="fcol" style="left:567px"><h5>MORE</h5><ul><li>OUR HISTORY</li><li>MY VEHICLE HISTORY</li><li>VERIFIED REVIEWS</li><li>TRUSTED BUSINESS</li></ul></div>
  <div class="fcol connect" style="left:824px"><h5>CONNECT</h5><ul>
    <li><i></i>555-014-2290</li>
    <li><i></i>SERVICE@HARBORPOINT.EXAMPLE</li>
    <li><i></i>2280 Lakeview Road, Fairhaven, Ohio 44190, United States</li>
    <li><i></i><span>Mon - Fri: 08:00 am – 05:00 pm<br>Mon - Fri: 08:00 am – 01:00 pm<br>Sun: CLOSED</span></li>
  </ul></div>
  <div class="rule"></div>
  <div class="legal"><span>Copyright © 2022 Harbor Point Repair and Towing - All Rights Reserved.</span><span>Built and Managed by Northline Web Studio</span></div>
</footer>

</body>
</html>
```